TalkNest Needs a Brochure Design

We need a brochure (sent as an e-mail message and via mail), to market our professional development seminars. We provide seminars related to autism and non-verbal communication. Brochure should have certain information (see Must Have Priorities) and be designed for target market.

Please submit only 2-3 of your best designs.
Updates

I have added a word file with detail information about the seminar. We want a design that can be sent both as e-mail and regular mail. A 8 x 10 design that can be folded and mailed will meet our requirements. We are hoping that we will be able to send the one page as an e-mail and the back can be used for advertisement.

Target Market(s)

Physicians, Speech-Language Pathologists, Occupational Therapist, Early Intervention Specialists, Special Educators.

Industry/Entity Type

Communication

Font styles to use
Sans Serif

Colors
3176b5
33b7a4
f68d4d

Requirements
Must have
• See the attached file. In addition the brochure must have:
1 Logo for academic accreditation and CEU information.
2. Registration Fees and how to register.
Nice to have
• Photographs.

```html
<!DOCTYPE html>
<html lang="en">
<head>
<meta charset="utf-8">
<title>TalkNest – Mobile Technology to Support Communication in Autism</title>
<link rel="stylesheet" href="https://fonts.googleapis.com/css2?family=Open+Sans:wght@400;600;700;800&family=Merriweather:wght@700;900&display=swap">
<style>
  :root{
    --brand-blue:#3176b5;
    --band-blue:#3a8fd6;
    --teal:#33b7a4;
    --orange:#f68d4d;
    --brand-green:#3fae49;
    --green-light:#8cc63f;
    --green-dark:#2e9a45;
    --ink:#3a3a3a;
    --ink-soft:#4a4a4a;
    --table-bg:#5d5d5d;
    --table-head:#4a4a4a;
    --table-line:#7a7a7a;
    --rule:#8a8a8a;
    --white:#ffffff;
    --page:#ffffff;
  }
  *{box-sizing:border-box;margin:0;padding:0}
  html,body{width:965px;height:1200px;overflow:hidden;background:var(--page)}
  body{font-family:"Open Sans",Arial,sans-serif;color:var(--ink);position:relative}

  .brochure{position:absolute;inset:0;width:965px;height:1200px;background:var(--white)}

  /* header */
  .brand{position:absolute;left:52px;top:78px;display:flex;align-items:center;gap:16px}
  .brand-mark{width:46px;height:46px;background:var(--brand-blue)}
  .brand-name{font-size:44px;font-weight:600;color:var(--brand-blue);letter-spacing:.5px}

  .provider{position:absolute;left:580px;top:34px;width:330px;height:150px;border:2px solid var(--ink);padding:8px;font-size:9.6px;line-height:1.3;color:var(--ink)}
  .provider-badge{float:left;width:108px;height:92px;background:#d9d9d9;border:2px solid var(--ink);margin:0 8px 4px 0}
  .provider strong{font-weight:700}

  .title{position:absolute;left:0;right:0;top:222px;text-align:center;font-family:"Merriweather",Georgia,serif;font-weight:900;font-size:44px;line-height:56px;color:var(--brand-blue);letter-spacing:.3px}

  .divider{position:absolute;left:0;right:0;top:390px;height:3px;background:var(--rule)}
  .agenda-tab{position:absolute;left:520px;top:368px;width:406px;height:48px;background:linear-gradient(180deg,var(--green-light),var(--green-dark));border-radius:24px 24px 4px 4px;color:var(--white);font-weight:700;font-size:24px;text-align:center;line-height:48px}

  /* left column */
  .section-bar{position:absolute;left:32px;width:460px;height:25px;background:linear-gradient(90deg,var(--green-dark),var(--green-light));border-radius:4px;color:var(--white);font-weight:700;font-size:17px;text-align:center;line-height:25px}
  .bar-instructor{top:434px}
  .bar-course{top:624px}
  .section-text{position:absolute;left:32px;width:460px;font-size:12.6px;line-height:18px;text-align:justify;color:var(--ink-soft)}
  .text-instructor{top:466px}
  .text-course{top:656px}

  .registration{position:absolute;left:32px;top:770px;width:460px;height:46px;border-left:5px solid var(--orange);background:#fff4ec;padding:5px 10px;font-size:11.8px;line-height:18px;color:var(--ink)}
  .registration strong{color:var(--teal);font-weight:800}
  .registration .fee{color:var(--orange);font-weight:800}

  /* agenda table */
  .agenda{position:absolute;left:536px;top:428px;width:380px;background:var(--table-bg);border-radius:4px;padding:6px;color:var(--white)}
  .agenda table{width:100%;border-collapse:collapse;font-size:11px;line-height:14.5px}
  .agenda th{background:var(--table-head);text-align:left;font-weight:600;padding:3px 6px}
  .agenda td{padding:3px 6px;vertical-align:top;border-top:1px solid var(--table-line)}
  .agenda td:first-child{width:132px;white-space:nowrap;border-right:1px solid var(--table-line)}
  .agenda th:first-child{border-right:1px solid var(--table-line)}

  /* lower band */
  .lower-band{position:absolute;left:0;right:0;top:825px;bottom:0;background:var(--band-blue)}
  .outcomes-panel{position:absolute;left:28px;top:840px;width:892px;height:340px;border-radius:8px;background:linear-gradient(100deg,var(--green-dark) 0%,var(--brand-green) 40%,var(--green-light) 100%)}
  .panel-split{position:absolute;left:472px;top:0;bottom:0;width:2px;background:rgba(255,255,255,.35)}
  .outcomes{position:absolute;left:20px;top:14px;width:430px;color:var(--white)}
  .outcomes h2{font-size:26px;font-weight:800;margin-bottom:4px}
  .outcomes .lead{font-size:13px;font-weight:600;margin-bottom:14px}
  .outcomes ul{list-style:none}
  .outcomes li{display:flex;gap:12px;font-size:13.6px;line-height:19px;margin-bottom:9px;padding-left:16px}
  .outcomes li svg{flex:none;margin-top:2px}

  .event-card{position:absolute;left:524px;top:22px;width:326px;height:298px;background:var(--white);padding:22px 20px;color:var(--ink)}
  .card-brand{display:flex;align-items:center;gap:10px;margin-bottom:24px}
  .card-brand .brand-mark{width:26px;height:26px}
  .card-brand .brand-name{font-size:26px}
  .event-card p{font-size:22px;font-weight:800;line-height:28px}
  .event-card .date{margin:10px 0 16px}
  .event-card .address{font-size:20px;line-height:26px}
</style>
</head>
<body>
<main class="brochure">
  <header>
    <div class="brand"><span class="brand-mark"></span><span class="brand-name">TalkNest</span></div>
    <aside class="provider">
      <div class="provider-badge" role="img" aria-label="Accreditation provider badge"></div>
      <strong>Clearpath Care Associates</strong> is approved by the Continuing Education Board of the National Speech and Hearing Council (NSHC) to provide continuing education activities in speech-language pathology and audiology. <strong>See course information for number of NSHC CEUs, instructional level and content area.</strong> NSHC CE Provider approval does not imply endorsement of course content, specific products or clinical procedures.
    </aside>
    <h1 class="title">MOBILE TECHNOLOGY TO SUPPORT<br>COMMUNICATION IN AUTISM</h1>
  </header>

  <div class="divider"></div>
  <div class="agenda-tab">Time-Ordered Agenda:</div>

  <h2 class="section-bar bar-instructor">Instructor:</h2>
  <p class="section-text text-instructor">Arjun Mehra is an Associate Professor of Communication Disorders at Lakeshore State University. He earned his doctorate from Westfield University. He has working experience in diverse settings including private practice, hospitals, long-term residential settings and integrated school-settings. His areas of research interest are: assistive technology, early language intervention, and reading disabilities. He has over 30 publications and over 100 presentations at national and international scientific meetings. He is a consulting editor for Assistive Communication Review.</p>

  <h2 class="section-bar bar-course">Course Description:</h2>
  <p class="section-text text-course">With the current availability of mobile technology (e.g., Orchard Tab, Nimbus OS) individuals with autism have many options available for communication. This course focused on visual support, accessibility, and language learning through mobile technology. Compared specialized AAC “apps” and assessed contemporary evidence for effective use of mobile technology by children with autism to enhance their communication skills.</p>

  <aside class="registration">
    <strong>Registration Fee:</strong> <span class="fee">$150</span> (students $95) &middot; 0.6 NSHC CEUs<br>
    <strong>How to Register:</strong> talknest.example/register or call (312) 555-0148
  </aside>

  <section class="agenda">
    <table>
      <thead><tr><th>Time</th><th>Topic</th></tr></thead>
      <tbody>
        <tr><td>8:30 am. - 9:00 am</td><td>Registration and Coffee</td></tr>
        <tr><td>9:00 am - 10:00 am</td><td>Information Processing, visual attention, and visual support in children with autism</td></tr>
        <tr><td>10:00 am - 10:45 am</td><td>Accessibility issues related to use of mobile technology</td></tr>
        <tr><td>10:45 am - 11:00 am</td><td>Break</td></tr>
        <tr><td>11:00 am - 12:00 noon</td><td>Language learning strategies using mobile technology</td></tr>
        <tr><td>12:00 noon - 12:30 pm</td><td>Lunch</td></tr>
        <tr><td>12:30 pm - 1:00 pm</td><td>Video presentations</td></tr>
        <tr><td>1:00 pm - 1:45 pm</td><td>Contemporary specialized AAC apps for children with autism</td></tr>
        <tr><td>1:45 pm - 2:00 pm</td><td>Break</td></tr>
        <tr><td>2:00 pm - 2:30 pm</td><td>Assessment of contemporary evidence for effectiveness of mobile technology</td></tr>
        <tr><td>2:30 pm - 3:00 pm</td><td>Wrap up discussion, questions, and comments</td></tr>
      </tbody>
    </table>
  </section>

  <div class="lower-band"></div>
  <section class="outcomes-panel">
    <div class="panel-split"></div>
    <div class="outcomes">
      <h2>Learner’s Outcomes:</h2>
      <p class="lead">As a result of this seminar, the participant will be able to:</p>
      <ul>
        <li><svg width="16" height="16" viewBox="0 0 16 16"><rect x="1" y="1" width="14" height="14" fill="none" stroke="#fff" stroke-width="1.5"/><path d="M4 8l3 3 6-7" fill="none" stroke="#fff" stroke-width="2"/></svg><span>Summarize issues related to information processing, visual attention, and visual support in children with autism.</span></li>
        <li><svg width="16" height="16" viewBox="0 0 16 16"><rect x="1" y="1" width="14" height="14" fill="none" stroke="#fff" stroke-width="1.5"/><path d="M4 8l3 3 6-7" fill="none" stroke="#fff" stroke-width="2"/></svg><span>Decide about accessibility of mobile technology by children with autism.</span></li>
        <li><svg width="16" height="16" viewBox="0 0 16 16"><rect x="1" y="1" width="14" height="14" fill="none" stroke="#fff" stroke-width="1.5"/><path d="M4 8l3 3 6-7" fill="none" stroke="#fff" stroke-width="2"/></svg><span>Integrate language learning strategies using mobile technology for children with autism.</span></li>
        <li><svg width="16" height="16" viewBox="0 0 16 16"><rect x="1" y="1" width="14" height="14" fill="none" stroke="#fff" stroke-width="1.5"/><path d="M4 8l3 3 6-7" fill="none" stroke="#fff" stroke-width="2"/></svg><span>Compare contemporary specialized AAC “apps” for children with autism.</span></li>
        <li><svg width="16" height="16" viewBox="0 0 16 16"><rect x="1" y="1" width="14" height="14" fill="none" stroke="#fff" stroke-width="1.5"/><path d="M4 8l3 3 6-7" fill="none" stroke="#fff" stroke-width="2"/></svg><span>Assess contemporary evidence for effectiveness of mobile technology by children with autism.</span></li>
      </ul>
    </div>
    <div class="event-card">
      <div class="card-brand"><span class="brand-mark"></span><span class="brand-name">TalkNest</span></div>
      <p>Speaker:&nbsp; Arjun Mehra<br>Ph.D., CCC-SLP</p>
      <p class="date">September 20, 2014</p>
      <p class="address">Location:<br>240 W Harbor Avenue,<br>Chicago, Il 60611</p>
    </div>
  </section>
</main>
</body>
</html>
```